Buchcover-Design für psychologischen Ratgeber Morgens voller Mut!
Zielgruppe
Veröffentlichung psychologischer Ratgeber. Zielgruppe sind Erwachsene.
Aufgabenstellung
keine besondere Vorgaben, ein eyecatching-Cover wäre super. Der Titel des Buches lautet: Morgens voller Mut! Der Untertitel lautet: Heitere Seelenkunde für mehr Ruhe und Zuversicht
Autoren: Dr. Hilde Marowski-Tappert, Dr. Jonas Tappert
Vielleicht macht es Sinn, einen Button mit: 199 Praxistipps auf dem Cover anzuführen.
Das Buch wird als Softcover und Ebook auf vendilo veröffentlicht. Das Format ist 6 mal 9 Zoll und hat 425 Seiten.

```html
<!DOCTYPE html>
<html lang="de">
<head>
<meta charset="utf-8">
<title>Morgens voller Mut! – Buchcover</title>
<link href="https://fonts.googleapis.com/css2?family=Londrina+Solid:wght@400&family=Fira+Sans+Condensed:wght@500;700;800&family=Roboto+Condensed:wght@500;700&display=swap" rel="stylesheet">
<style>
  :root {
    --paper: #ffffff;
    --band: #e29f1f;
    --cream: #f3efe6;
    --kicker: #ece5cf;
    --ink: #111111;
    --badge: #f7e80f;
    --badge-text: #ef7a17;
    --imprint: #111111;
  }
  html, body {
    margin: 0;
    padding: 0;
    overflow: hidden;
    background: var(--paper);
  }
  .cover {
    position: relative;
    width: 800px;
    height: 1200px;
    background: var(--paper);
    overflow: hidden;
  }

  /* Portrait wall */
  .portrait-grid {
    position: absolute;
    left: 12px;
    top: 12px;
    width: 776px;
    height: 618px;
    display: grid;
    grid-template-columns: repeat(5, 1fr);
    grid-template-rows: repeat(4, 1fr);
    gap: 4px;
  }
  .portrait {
    width: 100%;
    height: 100%;
    box-shadow: inset 0 0 38px rgba(40, 25, 10, 0.45);
  }
  .portrait::after { content: none; }
  .tone-blue     { background: radial-gradient(ellipse 60% 55% at 50% 38%, #f0d9c3 0%, #c9a88e 30%, #9bb7c9 55%, #4f7492 100%); }
  .tone-ochre    { background: radial-gradient(ellipse 60% 55% at 50% 38%, #f2d2b5 0%, #d0a47c 30%, #c9a360 55%, #8c6428 100%); }
  .tone-red      { background: radial-gradient(ellipse 60% 55% at 50% 38%, #d8ab8c 0%, #a77558 30%, #c9867a 55%, #8f4038 100%); }
  .tone-yellow   { background: radial-gradient(ellipse 60% 55% at 50% 38%, #f7dcc4 0%, #d9a37a 30%, #ecc660 55%, #b7841f 100%); }
  .tone-grey     { background: radial-gradient(ellipse 60% 55% at 50% 38%, #7a4f37 0%, #4a2e20 30%, #d5d2cc 55%, #858380 100%); }
  .tone-greyblue { background: radial-gradient(ellipse 60% 55% at 50% 38%, #f1d3bc 0%, #c7784a 30%, #b9c0c9 55%, #6e7b8a 100%); }
  .tone-sage     { background: radial-gradient(ellipse 60% 55% at 50% 38%, #f3d8c3 0%, #b88d62 30%, #cfcdb3 55%, #8c8b6c 100%); }
  .tone-rust     { background: radial-gradient(ellipse 60% 55% at 50% 38%, #f0c8a8 0%, #c99272 30%, #d09566 55%, #94562c 100%); }
  .tone-slate    { background: radial-gradient(ellipse 60% 55% at 50% 38%, #f0cdb3 0%, #8a6a52 30%, #8aa2bb 55%, #3f5e7e 100%); }
  .tone-royal    { background: radial-gradient(ellipse 60% 55% at 50% 38%, #f2cfb8 0%, #b9b2ab 30%, #5d7fc0 55%, #24478c 100%); }
  .tone-coral    { background: radial-gradient(ellipse 60% 55% at 50% 38%, #e7b596 0%, #7c5a45 30%, #df8a62 55%, #a64526 100%); }
  .tone-gold     { background: radial-gradient(ellipse 60% 55% at 50% 38%, #f3d3bf 0%, #4a3328 30%, #e6c46c 55%, #ad7f22 100%); }
  .tone-silver   { background: radial-gradient(ellipse 60% 55% at 50% 38%, #eccbb0 0%, #b48c52 30%, #cfd0d3 55%, #858a93 100%); }
  .tone-amber    { background: radial-gradient(ellipse 60% 55% at 50% 38%, #f2cfb1 0%, #9e6a40 30%, #e9c060 55%, #b0801e 100%); }
  .tone-tan      { background: radial-gradient(ellipse 60% 55% at 50% 38%, #f0d3bf 0%, #4b2e24 30%, #e2c08c 55%, #a57a3c 100%); }
  .tone-beige    { background: radial-gradient(ellipse 60% 55% at 50% 38%, #f1d7c3 0%, #dcd6cf 30%, #e2d8c6 55%, #a69678 100%); }
  .tone-lilac    { background: radial-gradient(ellipse 60% 55% at 50% 38%, #f2d3bd 0%, #8c6142 30%, #c3bddb 55%, #7a74a0 100%); }
  .tone-scarlet  { background: radial-gradient(ellipse 60% 55% at 50% 38%, #e8bc9c 0%, #2e2420 30%, #e08d6a 55%, #a2301f 100%); }
  .tone-honey    { background: radial-gradient(ellipse 60% 55% at 50% 38%, #f0d2bf 0%, #2e1f1a 30%, #e3c06e 55%, #a47a28 100%); }

  /* Tips badge */
  .tips-badge {
    position: absolute;
    left: 12px;
    top: 440px;
    width: 204px;
    height: 190px;
    overflow: hidden;
  }
  .tips-badge-disc {
    position: absolute;
    left: -40px;
    top: 28px;
    width: 250px;
    height: 250px;
    border-radius: 50%;
    background: var(--badge);
  }
  .tips-badge-text {
    position: absolute;
    left: 14px;
    top: 58px;
    margin: 0;
    transform: rotate(-8deg);
    transform-origin: left top;
    color: var(--badge-text);
    font-family: "Roboto Condensed", sans-serif;
    font-weight: 500;
    line-height: 1;
    white-space: nowrap;
  }
  .tips-badge-text .lead { font-size: 32px; }
  .tips-badge-text .count { font-size: 50px; font-weight: 700; }
  .tips-badge-text .label { display: block; font-size: 34px; margin-top: 0; }

  /* Title band */
  .title-band {
    position: absolute;
    left: 12px;
    top: 630px;
    width: 776px;
    height: 558px;
    background: var(--band);
  }
  .authors {
    position: absolute;
    top: 14px;
    left: 0;
    width: 100%;
    margin: 0;
    text-align: center;
    font-family: "Fira Sans Condensed", sans-serif;
    font-weight: 700;
    font-size: 23px;
    color: var(--ink);
  }
  .book-title {
    margin: 0;
    font-family: "Londrina Solid", sans-serif;
    font-weight: 400;
    color: var(--cream);
    text-shadow: 3px 5px 6px rgba(110, 60, 0, 0.4);
  }
  .book-title .line {
    position: absolute;
    left: 0;
    width: 100%;
    text-align: center;
    line-height: 1;
    white-space: nowrap;
  }
  .book-title .line-one { top: 62px; font-size: 104px; letter-spacing: 1px; }
  .book-title .line-two { top: 178px; font-size: 160px; letter-spacing: 4px; }
  .subtitle {
    position: absolute;
    top: 378px;
    left: 0;
    width: 100%;
    margin: 0;
    text-align: center;
  }
  .subtitle .kicker {
    display: block;
    font-family: "Fira Sans Condensed", sans-serif;
    font-weight: 800;
    font-size: 42px;
    letter-spacing: 6px;
    line-height: 1.1;
    color: var(--kicker);
  }
  .subtitle .claim {
    display: block;
    font-family: "Fira Sans Condensed", sans-serif;
    font-weight: 800;
    font-size: 44px;
    line-height: 1.1;
    color: var(--ink);
  }

  .imprint {
    position: absolute;
    left: 336px;
    top: 1120px;
    width: 132px;
    height: 80px;
    background: var(--imprint);
    display: flex;
    align-items: flex-end;
    justify-content: center;
    padding-bottom: 14px;
    box-sizing: border-box;
    color: #ffffff;
    font-family: "Fira Sans Condensed", sans-serif;
    font-weight: 500;
    font-size: 15px;
  }
</style>
</head>
<body>
<main class="cover">
  <section class="portrait-grid">
    <div class="portrait tone-blue" role="img" aria-label="Porträtfoto einer lächelnden Frau mit Locken"></div>
    <div class="portrait tone-ochre" role="img" aria-label="Porträtfoto eines lächelnden jungen Mannes"></div>
    <div class="portrait tone-red" role="img" aria-label="Porträtfoto eines lächelnden Mannes"></div>
    <div class="portrait tone-yellow" role="img" aria-label="Porträtfoto einer lächelnden Frau mit Schal"></div>
    <div class="portrait tone-grey" role="img" aria-label="Porträtfoto eines lachenden Mannes"></div>

    <div class="portrait tone-greyblue" role="img" aria-label="Porträtfoto eines Kindes mit Brille"></div>
    <div class="portrait tone-sage" role="img" aria-label="Porträtfoto einer jungen Frau"></div>
    <div class="portrait tone-rust" role="img" aria-label="Porträtfoto eines lachenden Mannes"></div>
    <div class="portrait tone-slate" role="img" aria-label="Porträtfoto eines jungen Mannes"></div>
    <div class="portrait tone-royal" role="img" aria-label="Porträtfoto eines älteren Herrn im Anzug"></div>

    <div class="portrait tone-coral" role="img" aria-label="Porträtfoto eines Mannes im Anzug"></div>
    <div class="portrait tone-gold" role="img" aria-label="Porträtfoto einer lächelnden Frau"></div>
    <div class="portrait tone-silver" role="img" aria-label="Porträtfoto eines Mannes mit Brille und Krawatte"></div>
    <div class="portrait tone-amber" role="img" aria-label="Porträtfoto eines lachenden jungen Mannes"></div>
    <div class="portrait tone-tan" role="img" aria-label="Porträtfoto einer lächelnden Frau"></div>

    <div class="portrait tone-ochre" role="img" aria-label="Porträtfoto einer lächelnden Person"></div>
    <div class="portrait tone-beige" role="img" aria-label="Porträtfoto eines lachenden älteren Herrn"></div>
    <div class="portrait tone-lilac" role="img" aria-label="Porträtfoto einer Frau mit Brille"></div>
    <div class="portrait tone-scarlet" role="img" aria-label="Porträtfoto einer Frau mit Federboa"></div>
    <div class="portrait tone-honey" role="img" aria-label="Porträtfoto einer Frau mit langen Haaren"></div>
  </section>

  <div class="tips-badge">
    <div class="tips-badge-disc"></div>
    <p class="tips-badge-text"><span class="lead">Mit </span><span class="count">199</span><span class="label">Praxistipps</span></p>
  </div>

  <section class="title-band">
    <p class="authors">Dr. Hilde Marowski-Tappert &amp; Dr. Jonas Tappert</p>
    <h1 class="book-title">
      <span class="line line-one">MORGENS VOLLER</span>
      <span class="line line-two">MUT!</span>
    </h1>
    <h2 class="subtitle">
      <span class="kicker">HEITERE SEELENKUNDE</span>
      <span class="claim">für mehr Ruhe &amp; Zuversicht</span>
    </h2>
  </section>

  <div class="imprint">Verlag Lichtblick</div>
</main>
</body>
</html>
```